label update for bottle change

The goal is to adapt the label's design and shape to the new bottle, maintaining its defining elements such as the font, vertical name, company logo, background pattern, and color. The new design should not be identical to the old one, but rather an evolution of it. The gold stripe on the bottom is not mandatory, but the writing "VALDORO DEL COLLE / EST. 1886" must be retained, slightly enlarged.

The font name is: Brandon Text

```html
<!DOCTYPE html>
<html lang="it">
<head>
<meta charset="utf-8">
<title>Amaro di Carattere Carciofo – Label Set</title>
<link rel="stylesheet" href="https://fonts.googleapis.com/css2?family=Montserrat:wght@500;600;700;800&family=Great+Vibes&display=swap">
<style>
  :root {
    --plum: #4b1056;
    --crimson: #a1194a;
    --gold: #d8b25a;
    --gold-deep: #b98f35;
    --white: #ffffff;
    --leaf: #2f6b3a;
    --paper: #ffffff;
    --sans: "Montserrat", "Helvetica Neue", Arial, sans-serif;
    --script: "Great Vibes", "Brush Script MT", cursive;
  }
  * { box-sizing: border-box; margin: 0; padding: 0; }
  html, body {
    width: 788px;
    height: 1200px;
    overflow: hidden;
    background: var(--paper);
  }
  .canvas {
    position: relative;
    width: 788px;
    height: 1200px;
  }

  /* Neck label */
  .neck-label {
    position: absolute;
    left: 268px;
    top: 40px;
    width: 252px;
    height: 152px;
    background: var(--plum);
    overflow: hidden;
  }
  .neck-label__title {
    position: absolute;
    left: 0;
    right: 0;
    top: 22px;
    text-align: center;
    font-family: var(--script);
    font-size: 38px;
    line-height: 1;
    color: var(--gold);
  }
  .neck-label__author {
    position: absolute;
    left: 0;
    right: 0;
    top: 82px;
    text-align: center;
    font-family: var(--sans);
    font-weight: 700;
    font-size: 15px;
    letter-spacing: 0.26em;
    color: var(--white);
  }

  /* Shared trim */
  .trim-line {
    position: absolute;
    left: 0;
    right: 0;
    height: 3px;
    background: linear-gradient(90deg, var(--gold-deep), var(--gold), var(--gold-deep));
  }
  .trim-band {
    position: absolute;
    left: 0;
    right: 0;
    background: var(--crimson);
  }
  .neck-label .trim-line { top: 121px; }
  .neck-label .trim-band { top: 125px; height: 27px; }

  /* Main label */
  .main-label {
    position: absolute;
    left: 51px;
    top: 228px;
    width: 686px;
    height: 924px;
    background: var(--plum);
    overflow: hidden;
  }
  .main-label__name {
    position: absolute;
    left: 0;
    top: 0;
  }
  .main-label__artwork {
    position: absolute;
    left: 280px;
    top: 126px;
    width: 370px;
    height: 598px;
    border-radius: 48% 48% 30% 30% / 40% 40% 20% 20%;
    background: linear-gradient(180deg, #a1194a 0%, #7a2a5c 35%, #c9a04e 60%, #3f6a3c 82%, #2f6b3a 100%);
  }
  .main-label__house {
    position: absolute;
    left: 0;
    right: 0;
    top: 778px;
    text-align: center;
    font-family: var(--sans);
    font-weight: 600;
    font-size: 30px;
    letter-spacing: 0.04em;
    color: var(--gold);
  }
  .main-label__est {
    position: absolute;
    left: 0;
    right: 0;
    top: 834px;
    display: flex;
    align-items: center;
    justify-content: center;
    gap: 16px;
    font-family: var(--sans);
    font-weight: 700;
    font-size: 17px;
    letter-spacing: 0.24em;
    color: var(--white);
  }
  .main-label__est::before,
  .main-label__est::after {
    content: "";
    width: 56px;
    height: 1px;
    background: var(--gold);
  }
  .main-label .trim-line { top: 890px; }
  .main-label .trim-band { top: 894px; height: 30px; }
</style>
</head>
<body>
<main class="canvas">

  <section class="neck-label">
    <p class="neck-label__title">Ode al carciofo</p>
    <p class="neck-label__author">PAOLO VERANI</p>
    <div class="trim-line"></div>
    <div class="trim-band"></div>
  </section>

  <section class="main-label">
    <svg class="main-label__name" width="686" height="924" viewBox="0 0 686 924" aria-label="Amaro di Carattere – Carciofo">
      <text transform="translate(134 712) rotate(-90)"
            textLength="490" lengthAdjust="spacingAndGlyphs"
            font-family="Montserrat, Helvetica Neue, Arial, sans-serif"
            font-weight="700" font-size="28" letter-spacing="5">
        <tspan fill="#d8b25a">AMARO </tspan><tspan fill="#d8b25a">DI </tspan><tspan fill="#d8b25a">CARATTERE</tspan>
      </text>
      <text transform="translate(242 712) rotate(-90)"
            textLength="608" lengthAdjust="spacingAndGlyphs"
            font-family="Montserrat, Helvetica Neue, Arial, sans-serif"
            font-weight="800" font-size="114" fill="#ffffff">CARCIOFO</text>
    </svg>

    <div class="main-label__artwork" role="img" aria-label="Engraved illustration of an artichoke in plum, gold and green"></div>

    <p class="main-label__house">Valdoro Del Colle</p>
    <p class="main-label__est">EST. 1886</p>

    <div class="trim-line"></div>
    <div class="trim-band"></div>
  </section>

</main>
</body>
</html>
```